Vorna Fleet business card

I am needing a business card that at a glance shows all the services that we provide emphasizing some more than others. We are a Fleet and Compliance management company as well as a software company. We provide outsourced solutions for KPX compliance and HR services via our own software.
In addition, we do
drug testing
GPS
Cameras
Electronic DVIRS
ELD's

Target Market(s)

Transportation company owners

Industry/Entity Type

Transportation supplier

Contact Information for Business Card

the card should inform potential customers what we do

Other font styles liked:
• I have added brand guidelines. See attached

Requirements
Must have
• See description
Should not have
• Colors outside my brand guide. See attached

```html
<!DOCTYPE html>
<html lang="en">
<head>
<meta charset="utf-8">
<title>Vorna Fleet business card</title>
<link href="https://fonts.googleapis.com/css2?family=Montserrat:wght@400;500;700;800&display=swap" rel="stylesheet">
<style>
  :root {
    --stage: #1c1c1c;
    --card: #262626;
    --card-edge: #e8262b;
    --brand-red: #e8262b;
    --ink-light: #ffffff;
    --ink-soft: #ececec;
    --emboss: #3a3a3a;
  }
  * { margin: 0; padding: 0; box-sizing: border-box; }
  html, body {
    width: 1200px; height: 900px; overflow: hidden;
    background: var(--stage);
    font-family: "Montserrat", sans-serif;
  }
  .canvas {
    width: 1200px; height: 900px;
    display: flex; flex-direction: column; align-items: center; justify-content: center;
    gap: 36px;
  }
  .card {
    width: 700px; height: 400px;
    background: linear-gradient(135deg, #2b2b2b 0%, var(--card) 60%, #232323 100%);
    border-radius: 18px;
    border-left: 2px solid var(--card-edge);
    border-bottom: 2px solid var(--card-edge);
    box-shadow: 0 14px 30px rgba(0,0,0,.55);
    position: relative;
  }
  .card-back { display: flex; align-items: center; justify-content: center; }
  .back-name {
    font-weight: 800; font-size: 64px; color: var(--emboss);
    letter-spacing: -1px;
  }
  .card-front { display: flex; align-items: center; padding: 0 50px 0 56px; }
  .brand {
    width: 290px; display: flex; align-items: center; gap: 12px;
  }
  .brand-dot { width: 18px; height: 18px; background: var(--brand-red); flex: none; }
  .brand-name {
    font-weight: 800; font-size: 44px; line-height: 1.02; color: var(--ink-light);
    letter-spacing: -0.5px;
  }
  .divider { width: 2px; height: 196px; background: var(--brand-red); margin: 0 36px 0 24px; }
  .contact { color: var(--ink-soft); }
  .contact-name {
    font-weight: 700; font-size: 24px; color: var(--brand-red);
    letter-spacing: 0.5px; text-transform: uppercase;
  }
  .contact-title { font-size: 17px; margin: 2px 0 16px; }
  .contact-address { font-size: 17px; line-height: 1.3; margin-bottom: 8px; }
  .contact-line { display: flex; align-items: center; gap: 8px; font-size: 17px; line-height: 1.5; }
  .contact-line svg { width: 13px; height: 13px; flex: none; }
</style>
</head>
<body>
<main class="canvas">
  <section class="card card-back">
    <span class="back-name">Vorna Fleet</span>
  </section>

  <section class="card card-front">
    <div class="brand">
      <span class="brand-dot"></span>
      <span class="brand-name">Vorna<br>Fleet</span>
    </div>
    <div class="divider"></div>
    <div class="contact">
      <p class="contact-name">Daniel Reyes</p>
      <p class="contact-title">Director</p>
      <p class="contact-address">4120 Harbor Loop, Ste B204<br>Ridgefield, OR 97321</p>
      <p class="contact-line">
        <svg viewBox="0 0 16 16"><path fill="#e8262b" d="M3 1l3 3-1.5 2a9 9 0 005 5L11.5 9.5l3 3-2 2.5C6 14 2 10 1 3z"/></svg>
        555-204-7713
      </p>
      <p class="contact-line">
        <svg viewBox="0 0 16 16"><rect x="4" y="1" width="8" height="4" fill="#e8262b"/><rect x="1" y="6" width="14" height="6" rx="1" fill="#e8262b"/><rect x="4" y="10" width="8" height="5" fill="#e8262b"/></svg>
        555-204-7719
      </p>
      <p class="contact-line">
        <svg viewBox="0 0 16 16"><rect x="1.5" y="3.5" width="13" height="9" fill="none" stroke="#e8262b" stroke-width="1.4"/><path d="M1.5 3.5L8 9l6.5-5.5" fill="none" stroke="#e8262b" stroke-width="1.4"/></svg>
        info@VornaFleet.com
      </p>
      <p class="contact-line">
        <svg viewBox="0 0 16 16"><circle cx="8" cy="8" r="6.5" fill="none" stroke="#e8262b" stroke-width="1.3"/><ellipse cx="8" cy="8" rx="2.8" ry="6.5" fill="none" stroke="#e8262b" stroke-width="1.1"/><path d="M1.5 8h13" stroke="#e8262b" stroke-width="1.1"/></svg>
        www.VornaFleet.com
      </p>
    </div>
  </section>
</main>
</body>
</html>
```